"Around the World " - Can you help us create our own wedding invitation?

I've had such great designs for my work projects from Pixel Harbor so when I couldn't find the perfect wedding invitation, I thought Id try opening it up to the experts! Please help us!
Description:
My fiancee and I come from different countries and have lived all over the world together so we would like our wedding invitation to be a map of the world, highlighted with pictograms of key places we've lived, all linked together to illustrate our story. The feel should be classic and elegant - not casual or cartoon-like. Ive attached to this brief some designs very similar to what we would like.
Specifics:
- Map of the world as a background - see attachments
- Pictograms: a house in Vancouver Canada, and a heart-shape in Sydney, Australia. Ski pictogram in Switzerland. Eiffel Tower pictogram in Paris. Pictogram of Statue of Liberty in New York. Pictogram of Mosque in Turkey. Pictogram of Small boat of coast of Turkey. Pictogram of diamond ring in Buenos Aires. Pictogram of paddle-boarder in Hawaii. Pictogram of 2 aeroplanes - one over water departing Sydney , One over water departing Vancouver creating a dotted line to the above destinations
- Colour palette: Black, white, grey/silver, shades of blue, mint green, taupe
- Text front: Milo and Dana - Sydney, Australia - 26 September 2014 (see attachment with the "postmark" idea!)
- Text back: Together with their families, Dana Pruitt and Milo Lindqvist request the honor of your presence at their wedding. Friday, the twenty-sixth of September, two thousand and fourteen at 4pm. The Bellmont Chapel at The Rocks. Dinner reception to follow at Marlows from 6pm.
- There should be some illustrative design elements on the rear side of the card also. See attachments.
Format:
- Appropriate resolution for printing on 4"x6" double sided postcard
- Require two final files: one file with the text as above, and another without the text i.e. blank.
Reason: Im sorry that I need to extend the deadline. I have a newborn baby with tonsillitis and it is difficult this week to provide feedback.

```html
<!DOCTYPE html>
<html lang="en">
<head>
<meta charset="utf-8">
<title>Wedding Invitation – Dana Pruitt &amp; Milo Lindqvist</title>
<link rel="stylesheet" href="https://fonts.googleapis.com/css2?family=Italianno&display=swap">
<style>
  :root {
    --page: #ffffff;
    --card: #f2eee5;
    --card-edge: #e6dfd0;
    --frame: #8a6a55;
    --ink: #7b5a47;
    --names: #93b39a;
    --heart: #a3263a;
    --rose-core: rgba(196, 180, 156, 0.62);
    --rose-mid: rgba(206, 193, 172, 0.42);
    --rose-fade: rgba(214, 203, 184, 0);
  }
  * { margin: 0; padding: 0; box-sizing: border-box; }
  html, body {
    width: 1200px;
    height: 900px;
    overflow: hidden;
    background: var(--page);
  }
  .canvas {
    position: relative;
    width: 1200px;
    height: 900px;
  }
  .invitation {
    position: absolute;
    left: 84px;
    top: 110px;
    width: 1040px;
    height: 684px;
    overflow: hidden;
    background: radial-gradient(ellipse at 50% 45%, #f6f3ec 0%, var(--card) 60%, var(--card-edge) 100%);
  }
  .invitation__frame {
    position: absolute;
    inset: 0;
    width: 100%;
    height: 100%;
  }
  .invitation__compass {
    position: absolute;
    left: 256px;
    top: 40px;
    width: 540px;
    height: 600px;
    border-radius: 50%;
    background:
      radial-gradient(circle at 50% 50%, var(--rose-core) 0%, var(--rose-mid) 30%, rgba(206,193,172,0.30) 42%, var(--rose-fade) 70%),
      radial-gradient(ellipse 12% 50% at 50% 50%, rgba(196,180,156,0.35) 0%, var(--rose-fade) 100%),
      radial-gradient(ellipse 50% 10% at 50% 50%, rgba(196,180,156,0.30) 0%, var(--rose-fade) 100%);
  }
  .invitation__heart {
    position: absolute;
    left: 508px;
    top: 66px;
    width: 56px;
    height: 48px;
  }
  .invitation__line {
    position: absolute;
    left: 0;
    width: 100%;
    text-align: center;
    font-family: "Italianno", cursive;
    font-weight: 400;
    color: var(--ink);
    font-size: 56px;
    line-height: 1;
    white-space: nowrap;
  }
  .invitation__names {
    color: var(--names);
    font-size: 84px;
  }
  .line--intro   { top: 126px; padding-right: 76px; }
  .line--names   { top: 202px; padding-left: 22px; }
  .line--request { top: 298px; padding-left: 40px; }
  .line--date    { top: 350px; padding-left: 40px; }
  .line--year    { top: 404px; padding-left: 40px; }
  .line--venue   { top: 458px; padding-left: 40px; }
  .line--dinner  { top: 554px; padding-left: 40px; }
</style>
</head>
<body>
<main class="canvas">
  <section class="invitation">
    <svg class="invitation__frame" viewBox="0 0 1040 684" aria-hidden="true">
      <g fill="none" stroke="var(--frame)" stroke-width="1.4" opacity="0.75">
        <line x1="4" y1="28" x2="1036" y2="28"/>
        <line x1="4" y1="646" x2="1036" y2="646"/>
        <line x1="28" y1="4" x2="28" y2="680"/>
        <line x1="1012" y1="4" x2="1012" y2="680"/>
        <line x1="14" y1="38" x2="1026" y2="38"/>
        <line x1="14" y1="636" x2="1026" y2="636"/>
        <line x1="40" y1="14" x2="40" y2="670"/>
        <line x1="1000" y1="14" x2="1000" y2="670"/>
      </g>
    </svg>

    <div class="invitation__compass" role="img" aria-label="Large faint taupe compass rose illustration behind the invitation text"></div>

    <svg class="invitation__heart" viewBox="0 0 56 48" aria-hidden="true">
      <path d="M28 46 C10 32 2 24 2 14 C2 6 8 1 15 1 C21 1 26 5 28 10 C30 5 35 1 41 1 C48 1 54 6 54 14 C54 24 46 32 28 46 Z" fill="var(--heart)"/>
    </svg>

    <p class="invitation__line line--intro">Together with their families,</p>
    <h1 class="invitation__line invitation__names line--names">Dana Pruitt &amp; Milo Lindqvist</h1>
    <p class="invitation__line line--request">request the honor of your presence at their wedding.</p>
    <p class="invitation__line line--date">Friday, the twenty-sixth of September</p>
    <p class="invitation__line line--year">two thousand and fourteen at 4 pm.</p>
    <p class="invitation__line line--venue">The Bellmont Chapel at the Rocks.</p>
    <p class="invitation__line line--dinner">Dinner reception to follow at Marlows from 6 pm.</p>
  </section>
</main>
</body>
</html>
```